Bref créative
Law firm stationary package
Letterhead, business card, envelope
Professional
Theodore R. Wexley
Attorney at Law
5183 Poldin Lane, Suite A
P.O. Box 81947
Cincinnati, OH 45867
Ted@WexleyCounsel.example
www.WexleyCounsel.example
Please create business card, letterhead, and envelope designs.
Focus on clean, professional design for this corporate law firm. Stay away from watermarks, waves, or anything that is too ink-intensive. You may use either or both of the attached logos.
Main logo
Inverse of logo, use is optional

```html
<!DOCTYPE html>
<html lang="en">
<head>
<meta charset="utf-8">
<title>Wexley Counsel, LLC — Business Card</title>
<link rel="stylesheet" href="https://fonts.googleapis.com/css2?family=Cinzel:wght@400;600&family=Cormorant+Garamond:ital,wght@0,500;1,500&display=swap">
<style>
  :root {
    --backdrop: #3b3b3d;
    --brand-blue: #2c2f8e;
    --brand-blue-dark: #23267a;
    --card-white: #f4f4f5;
    --text-grey: #6a6a70;
    --rule-grey: #b9b9c0;
    --paper-white: #ffffff;
  }
  * { margin: 0; padding: 0; box-sizing: border-box; }
  html, body {
    width: 1200px; height: 874px; overflow: hidden;
    background: var(--backdrop);
  }
  .canvas {
    position: relative; width: 1200px; height: 874px;
  }
  .card {
    position: absolute; left: 250px; width: 700px; height: 400px;
    box-shadow: 0 10px 30px rgba(0,0,0,0.45);
  }
  /* Back side */
  .card-back {
    top: 22px;
    background: linear-gradient(160deg, var(--brand-blue) 0%, var(--brand-blue-dark) 100%);
    display: flex; flex-direction: column; align-items: center; justify-content: center;
    gap: 22px;
  }
  .back-square {
    width: 64px; height: 64px; background: var(--paper-white); border-radius: 8px;
  }
  .back-name {
    font-family: "Cinzel", serif; font-weight: 400; font-size: 30px;
    letter-spacing: 4px; color: var(--paper-white);
  }
  /* Front side */
  .card-front {
    top: 452px; background: var(--card-white);
  }
  .brand {
    position: absolute; left: 58px; top: 62px; display: flex; align-items: center;
  }
  .brand-square {
    width: 58px; height: 58px; background: var(--brand-blue); border-radius: 6px;
  }
  .brand-rule {
    width: 1px; height: 96px; background: var(--rule-grey); margin: 0 22px;
  }
  .brand-name {
    font-family: "Cinzel", serif; font-weight: 400; color: var(--brand-blue);
    line-height: 1;
  }
  .brand-name .firm { display: block; font-size: 44px; letter-spacing: 1px; }
  .brand-name .suffix { display: block; font-size: 14px; letter-spacing: 3px; text-align: right; margin-top: 8px; }
  .contact-list {
    position: absolute; left: 488px; top: 66px; list-style: none;
    font-family: "Cormorant Garamond", serif; font-weight: 500; font-size: 13px;
    line-height: 1.55; color: var(--text-grey);
  }
  .holder {
    position: absolute; left: 160px; top: 232px;
  }
  .holder-name {
    font-family: "Cinzel", serif; font-weight: 600; font-size: 19px;
    letter-spacing: 1px; color: var(--brand-blue);
  }
  .holder-title {
    font-family: "Cormorant Garamond", serif; font-style: italic; font-weight: 500;
    font-size: 14px; color: var(--brand-blue); margin: 2px 0 14px 48px;
  }
  .holder-address {
    font-family: "Cormorant Garamond", serif; font-weight: 500; font-size: 14px;
    line-height: 1.5; color: var(--text-grey); font-style: normal; text-align: right;
  }
  .web {
    position: absolute; left: 488px; top: 168px;
    font-family: "Cormorant Garamond", serif; font-weight: 500; font-size: 13px; color: var(--text-grey);
  }
</style>
</head>
<body>
<main class="canvas">
  <section class="card card-back" aria-label="Business card, back">
    <div class="back-square"></div>
    <div class="back-name">WEXLEY COUNSEL</div>
  </section>

  <section class="card card-front" aria-label="Business card, front">
    <div class="brand">
      <div class="brand-square"></div>
      <div class="brand-rule"></div>
      <div class="brand-name">
        <span class="firm">WEXLEY</span>
        <span class="suffix">COUNSEL, LLC</span>
      </div>
    </div>
    <ul class="contact-list">
      <li>Tel: 513.555.0142</li>
      <li>Fax: 513.555.0187</li>
      <li>Cell: 513.555.0163</li>
      <li>Email: Ted@WexleyCounsel.example</li>
    </ul>
    <div class="web">www.WexleyCounsel.example</div>
    <div class="holder">
      <div class="holder-name">Theodore R. Wexley</div>
      <div class="holder-title">Attorney at Law</div>
      <address class="holder-address">
        5183 Poldin Lane, Suite A<br>
        P.O. Box 81947 · Cincinnati, OH 45867
      </address>
    </div>
  </section>
</main>
</body>
</html>
```